Corvane Medical Business Card Design

This is a private medical device company. We recently launched the new website and would like to redesign the business cards. Please see the website: www.corvanemedical.example. We'd like to keep the cards simple and professional but modern to match the website and collateral branding. Our customers are physicians and investors. I have attached the old design for comparison. I have also attached the updated logo. Please note the business card information will change, based on all employees who need to order them. So I will need to be able easily edit the copy.
Updates

Hi designers-thank you very much for submitting designs. I look forward to the results!! Joan

Target Market(s)

Our target audience are physicians

Industry/Entity Type

Medical

Contact Information for Business Card

Dorothy Wensley
Director of Marketing and Reimbursement
dwensley@corvanemedical.example
M: xxx-xxx-xxxx
O: xxx-xxx-xxxx
4120 Pinto Ridge Rd.
Suite 610
Austin, TX 78592

Font styles to use
Sans Serif

Requirements
Must have
• Must include the logo and a color or color from the logo and branding
Nice to have
• Maybe include the logo icon on the back.

```html
<!DOCTYPE html>
<html lang="en">
<head>
<meta charset="utf-8">
<title>Corvane Medical Business Card</title>
<link rel="stylesheet" href="https://fonts.googleapis.com/css2?family=Open+Sans:wght@400;600&display=swap">
<style>
  :root {
    --backdrop: #e6e6e6;
    --card: #ffffff;
    --ink: #231f20;
    --ink-soft: #3f3b3c;
    --teal: #78b8c9;
    --charcoal: #4b4647;
  }
  * { margin: 0; padding: 0; box-sizing: border-box; }
  html, body {
    width: 1044px;
    height: 1200px;
    overflow: hidden;
    background: var(--backdrop);
    font-family: "Open Sans", sans-serif;
    color: var(--ink);
  }
  .card {
    position: absolute;
    left: 146px;
    width: 758px;
    height: 444px;
    background: var(--card);
    overflow: hidden;
  }
  .card-front { top: 115px; }
  .card-back { top: 614px; }

  .brand {
    display: flex;
    align-items: center;
    color: var(--charcoal);
    font-weight: 600;
    white-space: nowrap;
  }
  .brand-dot {
    border-radius: 50%;
    background: var(--teal);
    flex: none;
  }
  .brand-front {
    position: absolute;
    left: 0; right: 0; top: 0; bottom: 0;
    justify-content: center;
    gap: 22px;
    font-size: 54px;
    letter-spacing: -0.5px;
  }
  .brand-front .brand-dot { width: 70px; height: 70px; }

  .contact {
    position: absolute;
    right: 402px;
    top: 0;
    text-align: right;
    white-space: nowrap;
  }
  .contact-name {
    position: absolute; right: 0; top: 70px;
    font-size: 22px; font-weight: 600; color: var(--ink);
  }
  .contact-title {
    position: absolute; right: 0; top: 108px;
    font-size: 13px; color: var(--ink-soft);
  }
  .contact-line {
    position: absolute; right: 0;
    font-size: 14px; color: var(--ink-soft);
  }
  .contact-email { top: 210px; }
  .contact-phones { top: 234px; word-spacing: 2px; }
  .contact-phones span + span { margin-left: 18px; }
  .contact-web { top: 318px; }
  .contact-address { top: 342px; }

  .divider {
    position: absolute;
    left: 400px; top: 80px;
    width: 2px; height: 282px;
    background: var(--teal);
  }
  .brand-back {
    position: absolute;
    left: 428px; top: 208px;
    gap: 14px;
    font-size: 30px;
  }
  .brand-back .brand-dot { width: 44px; height: 44px; }

  .band {
    position: absolute;
    bottom: 0; height: 16px;
  }
  .band-teal { left: 0; width: 315px; background: var(--teal); }
  .band-charcoal { left: 315px; right: 0; background: var(--charcoal); }
</style>
</head>
<body>
  <section class="card card-front">
    <div class="brand brand-front">
      <span class="brand-dot"></span>
      <span class="brand-name">Corvane Medical</span>
    </div>
  </section>

  <section class="card card-back">
    <div class="contact">
      <p class="contact-name">Dorothy Wensley</p>
      <p class="contact-title">Director of Marketing and Reimbursement</p>
      <p class="contact-line contact-email">dwensley@corvanemedical.example</p>
      <p class="contact-line contact-phones"><span>M: xxx-xxx-xxxx</span><span>O: xxx-xxx-xxxx</span></p>
      <p class="contact-line contact-web">www.corvanemedical.example</p>
      <p class="contact-line contact-address">4120 Pinto Ridge Rd. Suite 610 Austin, TX 78592</p>
    </div>
    <div class="divider"></div>
    <div class="brand brand-back">
      <span class="brand-dot"></span>
      <span class="brand-name">Corvane Medical</span>
    </div>
    <div class="band band-teal"></div>
    <div class="band band-charcoal"></div>
  </section>
</body>
</html>
```